Fahrzeugbeschriftung für Fahrschule gesucht
Ich bin sehr sehr zufrieden mit dem Ergebnis.Die wünsche die ich hatte wurden ohne zu zögern gleich umgesetzt. Der Designer arbeitet schnell und Präzise. Sehr gerne wieder für zukünftige Projekte!!
Zielgruppe
Meine Firma ist eine Fahrschule. Name der Fahrschule ist ZACK. Die Fahrschule befindet sich in Heidelberg am Neckar. Wir bilden alle Motorradklassen, PKW Klassen und Anhänger für PKW aus.
Unsere Zielgruppe sind hauptsächlich Jugendliche von 16-25 Jahren.
Aufgabenstellung
Unsere Fahrzeuge sind Schwarz, der Anhänger soll als Werbefläche für die Fahrschule dienen und soll auffallen. Das Grundelement des Designs sollte eher dunkel bleiben. Der Anhänger ist weiß und soll schwarz foliert bzw. Eure Ideen soll auf die Folie drauf und das auf den Anhänger.Ich bin Motorrad begeistert und brenne für meinen Job.
Ich möchte gerne mein Logo in Illustrationen einbauen. Das Logo soll bitte auch im Grafitti Stil sein
Hier ein link als Beispiele
https://www.bildquellora.com/de/grafiken/graffiti-hintergrund?sort=best&mediatype=illustration&assetfiletype=eps&phrase=Graffiti%20Hintergrund

```html
<!DOCTYPE html>
<html lang="de">
<head>
<meta charset="utf-8">
<title>Fahrschule ZACK – Anhängerbeschriftung</title>
<link href="https://fonts.googleapis.com/css2?family=Roboto+Condensed:ital,wght@0,700;1,700&display=swap" rel="stylesheet">
<style>
  :root {
    --stage: #e6e6e6;
    --panel: #ffffff;
    --orange: #f0902a;
    --orange-deep: #e07f1c;
    --ink: #111111;
    --road: #1e1e1e;
  }
  * { margin: 0; padding: 0; box-sizing: border-box; }
  html, body { width: 905px; height: 1200px; overflow: hidden; background: var(--stage); }
  .canvas { position: relative; width: 905px; height: 1200px; font-family: "Roboto Condensed", "Arial Narrow", sans-serif; color: var(--ink); }
  .door { position: absolute; top: 86px; height: 998px; background: var(--panel); overflow: hidden; }
  .door--left { left: 50px; width: 395px; }
  .door--right { left: 518px; width: 352px; }
  .band { position: absolute; top: 0; left: 0; width: 100%; display: block; }
  .brand { position: absolute; top: 250px; left: 0; width: 100%; text-align: center; font-weight: 700; font-size: 38px; letter-spacing: 1px; text-transform: uppercase; color: var(--ink); }
  .phone { position: absolute; top: 385px; left: 0; width: 100%; text-align: center; font-style: italic; font-weight: 700; font-size: 46px; }
  .email { position: absolute; top: 458px; left: 0; width: 100%; text-align: center; font-style: italic; font-weight: 700; font-size: 33px; }
  .road-art { position: absolute; left: 0; bottom: 0; width: 100%; height: 360px; background: linear-gradient(160deg, rgba(255,255,255,0) 25%, #3a3a3a 60%, var(--road) 100%); }
  .classes-title { position: absolute; top: 200px; left: 0; width: 100%; text-align: center; font-style: italic; font-weight: 700; font-size: 38px; }
  .classes { position: absolute; top: 268px; left: 79px; width: 190px; display: grid; grid-template-columns: 1fr 1fr; row-gap: 12px; font-weight: 700; font-size: 44px; line-height: 48px; }
  .classes .right { text-align: right; }
  .website { position: absolute; top: 870px; left: 0; width: 100%; text-align: center; font-style: italic; font-weight: 700; font-size: 27px; }
</style>
</head>
<body>
<div class="canvas">
  <section class="door door--left">
    <svg class="band" width="395" height="230" viewBox="0 0 395 230" role="img" aria-label="Orangefarbenes Zielflaggen-Karomuster als Kopfband">
      <defs>
        <linearGradient id="bandL" x1="0" y1="0" x2="1" y2="1">
          <stop offset="0" stop-color="var(--orange)"/>
          <stop offset="1" stop-color="var(--orange-deep)"/>
        </linearGradient>
      </defs>
      <path d="M0 0 H395 V95 C260 110 110 160 0 215 Z" fill="url(#bandL)"/>
    </svg>
    <div class="brand">Fahrschule ZACK</div>
    <div class="phone">0176-41 928 57</div>
    <div class="email">Info@fahrschule-zack.de</div>
    <div class="road-art" role="img" aria-label="Illustration einer geschwungenen schwarzen Straße mit weißen Markierungen"></div>
  </section>

  <section class="door door--right">
    <svg class="band" width="352" height="120" viewBox="0 0 352 120" role="img" aria-label="Orangefarbenes Zielflaggen-Karomuster als Kopfband">
      <defs>
        <linearGradient id="bandR" x1="0" y1="0" x2="1" y2="1">
          <stop offset="0" stop-color="var(--orange)"/>
          <stop offset="1" stop-color="var(--orange-deep)"/>
        </linearGradient>
      </defs>
      <path d="M0 0 H352 V62 C240 62 110 64 0 78 Z" fill="url(#bandR)"/>
    </svg>
    <h2 class="classes-title">Ausbildungsklassen</h2>
    <div class="classes">
      <span>AM</span><span class="right">B</span>
      <span>A1</span><span class="right">BE</span>
      <span>A2</span><span class="right">B96</span>
      <span>A</span><span class="right">B196</span>
    </div>
    <div class="website">WWW.FAHRSCHULE-ZACK.DE</div>
  </section>
</div>
</body>
</html>
```